Pell's Lodge & Grill Burger Restaurant Website - HomePage Only PSD

I need a website design for a restaurant called "Pell's Lodge and Grill" featuring burgers, wings, beer, live music, trivia, and more. I have several images of the restaurant and they already have their logo files created (see attached). I want some type of wood background and integrate the silver tin. This needs to be a modern, hip and fun type design. Design must incorporate these attached graphics.

UPDATE - just added a few more images of things I really like to be incorporated into my designs.
Updates

Industry/Entity Type

Burger Restaurant

Number of Pages Required

1 page

Font styles to use
Sans Serif

Requirements
Must have
• Restaurant/Bar theme with integration of existing logo and the red wood look.
Nice to have
• - Modern Fun appearance
• - Use Andy Fonts

```html
<!DOCTYPE html>
<html lang="en">
<head>
<meta charset="utf-8">
<title>Pell's Lodge and Grill</title>
<link href="https://fonts.googleapis.com/css2?family=Open+Sans:wght@400;600&family=PT+Serif:wght@400;700&family=Pinyon+Script&display=swap" rel="stylesheet">
<style>
:root{
  --wood:#8a4a22;
  --tin:#e9e9ea;
  --ink:#2a2a2a;
  --muted:#777;
  --bar:#2b2523;
  --footer:#b0622a;
  --accent:#d6b62a;
  --white:#fff;
}
*{margin:0;padding:0;box-sizing:border-box}
html,body{width:786px;height:1200px;overflow:hidden}
body{position:relative;background:var(--white);font-family:"Open Sans",sans-serif;color:var(--ink)}
.abs{position:absolute}
.wood-band{left:0;top:0;width:786px;height:244px;
  background:repeating-linear-gradient(90deg,#7a3e1c 0 3px,#8d4b24 3px 38px,#6e3618 38px 40px,#955228 40px 78px);}
.tin-band{left:0;top:244px;width:786px;height:336px;
  background:repeating-linear-gradient(90deg,#f3f3f4 0 6px,#e4e4e6 6px 8px),var(--tin);}
.nav{left:126px;top:50px;width:540px;height:30px;background:var(--bar);font-size:9px;color:var(--white)}
.nav a{color:var(--white);text-decoration:none;position:absolute;top:10px}
.nav .active{border-bottom:1px solid var(--white);padding-bottom:6px}
.hero{left:126px;top:80px;width:540px;height:256px;
  background:radial-gradient(ellipse at 65% 55%,#7a3a1c 0%,#4a2612 45%,#2a1a10 100%);
  clip-path:path("M0 0 H540 V236 Q270 272 0 236 Z");}
.hero-title{left:126px;top:156px;width:540px;text-align:center;font-family:"PT Serif",serif;font-size:31px;color:var(--white)}
.hero-sub{left:126px;top:196px;width:540px;text-align:center;font-family:"PT Serif",serif;font-size:17px;color:var(--white)}
.hero-curve{left:125px;top:306px}
.dots{left:366px;top:316px;display:flex;gap:4px}
.dots span{width:10px;height:10px;border-radius:50%;background:var(--white)}
.dots span:first-child{background:var(--accent);border:2px solid var(--white)}
.logo{left:344px;top:14px;width:102px;height:102px;border-radius:50%;background:var(--white);border:3px solid var(--bar);
  display:flex;align-items:center;justify-content:center;text-align:center;font-family:"PT Serif",serif;font-weight:700;font-size:13px;line-height:1.2;color:var(--bar)}
.welcome{left:0;top:362px;width:786px;text-align:center}
.welcome .script{font-family:"Pinyon Script",cursive;font-size:24px;position:relative;display:inline-block}
.welcome .script::before,.welcome .script::after{content:"";position:absolute;top:17px;width:70px;border-top:1px solid #555}
.welcome .script::before{right:100%;margin-right:4px}
.welcome .script::after{left:100%;margin-left:4px}
.welcome h1{font-family:"PT Serif",serif;font-weight:400;font-size:20px;margin-top:-2px}
.welcome p{width:490px;margin:14px auto 0;font-size:8px;line-height:14px;color:var(--muted)}
.feature{top:486px;width:182px;height:130px;color:var(--white);text-align:center}
.feature .frame{position:absolute;left:5px;top:4px;right:5px;bottom:5px;border:1px solid var(--white)}
.feature h3{margin-top:50px;font-weight:400;font-size:13px}
.feature p{font-size:7px;line-height:13px;padding:0 24px}
.f1{left:119px;background:linear-gradient(135deg,#3a1f3e,#6b3a6a 50%,#2a1530)}
.f2{left:302px;background:linear-gradient(180deg,#4a3a3a,#8a7a6a 60%,#c8c2b8)}
.f3{left:484px;background:linear-gradient(160deg,#6a4a2a,#b8802e 55%,#4a3018)}
.about-photo{left:114px;top:630px;width:216px;height:216px;border-radius:50%;border:1px solid #ddd;padding:5px;background:var(--white)}
.about-photo div{width:100%;height:100%;border-radius:50%;background:linear-gradient(160deg,#6a8fb8,#9a5a3a 60%,#7a3e24)}
.about{left:344px;top:656px;width:320px}
.about h2{font-family:"PT Serif",serif;font-weight:400;font-size:20px;margin-left:2px}
.about p{font-size:9px;line-height:14px;color:var(--muted)}
.about .lead{margin-top:10px}
.about .body{margin-top:16px;font-size:8px}
.btn{display:inline-block;margin-top:14px;border:1px solid var(--ink);border-radius:13px;padding:5px 13px;font-size:9px;color:var(--ink);text-decoration:none}
.gallery{left:0;top:885px;width:786px;height:209px;
  background:repeating-linear-gradient(180deg,#3a2418 0 5px,#24160e 5px 9px,#4a2e1e 9px 16px,#1c120b 16px 18px);}
.mini-logo{left:370px;top:864px;width:46px;height:46px;border-radius:50%;background:var(--white);border:2px solid var(--bar);
  display:flex;align-items:center;justify-content:center;text-align:center;font-family:"PT Serif",serif;font-weight:700;font-size:6px;line-height:1.15;color:var(--bar)}
.gallery-title{left:0;top:917px;width:786px;text-align:center;font-family:"PT Serif",serif;font-size:16px;color:var(--white)}
.thumb{top:958px;width:129px;height:88px;border:3px solid var(--white)}
.t1{left:129px;background:linear-gradient(135deg,#e08a2a,#b5401a 60%,#7a2a10)}
.t2{left:266px;background:linear-gradient(135deg,#c83a8a,#4a3aa8 60%,#2a2a6a)}
.t3{left:401px;background:linear-gradient(135deg,#5a6a7a,#8a6a5a 50%,#3a4a5a)}
.t4{left:537px;background:linear-gradient(150deg,#4a5478,#7a5a58 55%,#5a4a40)}
.footer{left:0;top:1094px;width:786px;height:106px;background:var(--footer);color:var(--white);text-align:center}
.footer nav{margin-top:24px;font-size:9px}
.footer nav a{color:var(--white);text-decoration:none;margin:0 11px}
.footer small{display:block;margin-top:8px;font-size:7px;color:#f0d6c0}
.social{display:flex;justify-content:center;gap:4px;margin-top:10px}
.social span{width:17px;height:17px;border:1px solid var(--white);border-radius:50%}
</style>
</head>
<body>
<div class="abs wood-band"></div>
<div class="abs tin-band"></div>

<div class="abs hero" role="img" aria-label="Close-up photo of a burger"></div>
<div class="abs hero-title">Great Food, Wine &amp; Music</div>
<div class="abs hero-sub">Maecenas aliquet turpis Mauris</div>
<svg class="abs hero-curve" width="542" height="40" viewBox="0 0 542 40">
  <path d="M0 14 Q271 48 542 14" fill="none" stroke="#2b2523" stroke-width="2"/>
</svg>
<div class="abs dots"><span></span><span></span><span></span><span></span></div>

<nav class="abs nav">
  <a class="active" style="left:21px">HOME</a>
  <a style="left:72px">ABOUT US</a>
  <a style="left:142px">OUR SERVICE</a>
  <a style="left:340px">OUR MENU</a>
  <a style="left:413px">GALLERY</a>
  <a style="left:477px">CONTACT</a>
</nav>
<div class="abs logo">Pell's<br>Lodge and<br>Grill</div>

<section class="abs welcome">
  <div class="script">Welcome</div>
  <h1>PELL'S LODGE AND GRILL</h1>
  <p>Maecenas aliquet velit vel turpis Mauris neque metus malesuada nec ultricies sit amet porttitor mattis enim In massa libero interdum nec interdum vel blandit sed nulla In ullamcorper est eget tempor cursus neque mi conse</p>
</section>

<div class="abs feature f1" role="img" aria-label="Live music photo"><div class="frame"></div><h3>LIVE MUSIC</h3><p>Maecenas aliquet velit vel turpis Mauris neque metus malesuada nec</p></div>
<div class="abs feature f2" role="img" aria-label="Burgers and wings photo"><div class="frame"></div><h3>BURGERS &amp; WINGS</h3><p>Maecenas aliquet velit vel turpis Mauris neque metus malesuada nec</p></div>
<div class="abs feature f3" role="img" aria-label="Beer glasses photo"><div class="frame"></div><h3>BEER &amp; TRIVIA</h3><p>Maecenas aliquet velit vel turpis Mauris neque metus malesuada</p></div>

<div class="abs about-photo"><div role="img" aria-label="Photo of the restaurant building"></div></div>
<section class="abs about">
  <h2>About Our Restaurant</h2>
  <p class="lead">Maecenas aliquet velit vel turpis Mauris neque metus malesuada nec ultricies sit amet porttitor mattis enim In massa libero</p>
  <p class="body">Praesent elementum elit at tellus Curabitur metus ipsum luctus eu malesuada ut tincidunt sed diam Donec quis mi sed magna hendrerit accumsan Suspendisse risus nibh ultricies eu volutpat non condimentum hendrerit augue Etiam eleifend metus vitae adipiscing semper mauris ipsum iaculis elit congu</p>
  <a class="btn">Learn More</a>
</section>

<div class="abs gallery"></div>
<div class="abs mini-logo">Pell's<br>Lodge and<br>Grill</div>
<div class="abs gallery-title">OUR GALLERY</div>
<div class="abs thumb t1" role="img" aria-label="Gallery photo of wings"></div>
<div class="abs thumb t2" role="img" aria-label="Gallery photo of a guitar on stage"></div>
<div class="abs thumb t3" role="img" aria-label="Gallery photo of wall art"></div>
<div class="abs thumb t4" role="img" aria-label="Gallery photo of the dining room"></div>

<footer class="abs footer">
  <nav><a>HOME</a><a>ABOUT US</a><a>OUR SERVICE</a><a>OUR MENU</a><a>GALLERY</a><a>CONTACT</a></nav>
  <small>© 2016 Company Name&nbsp; All right reserved&nbsp; Term of Use</small>
  <div class="social"><span></span><span></span><span></span><span></span></div>
</footer>
</body>
</html>
```